Qorvel Consulting

We focus on Data Recovery but we also do Network Security. We recover data from all types of hard drive form factors 3.5", 2.5", 1", 1.8", 5.25", 8" with any kind of interface IDE(PATA), SATA, mSATA, SCSI, SAS and Fibre Channel. All RAID Arrays 0, 1, 2, 3, 4, 5, 10 including nested levels like RAID 0+1, 1+0, 100, 0+3, 50 and 60, flash drives, like tablets, cellphones, usb drives, memory cards(SD, miniSD, Data Wafer(tavik))

Actually you can gather any information or text from any data recovery site, cause is usually the same info, we would probably change a couple of things from the description so it wont look the same. One thing though, we want to make clear to users not to attempt data recovery themselves and to ship the faulty device to us, maybe we can illustrate this?

the Data Recovery link can have sub menus like "Data Recovery Process - Data Recovery Services - F.A.Q"

the Penetration Testing can have sub menus like "F.A.Q - Pentest Process - Pentest Services"

Here are links from website so you gather information:

-http://www.mydiskwentdark.example/

-http://www.bitrescuelabsrecovery.example/

-http://www.pulvenbytes.example/

http://fetchlostfiles.example/lp/hard-drive-recovery.aspx?src=Brovix&gclid=ZTRWq4XplnQMDA-kwPbcf7HE2s
http://www.qulm.example/
http://www.venbrisfield.example/data-recovery/
http://www.tzwdatarecovery.example/

thanks.

Target Market(s)

Any PC user

Industry/Entity Type

Data Recovery

Requirements
Must have
• - Language and geographic navigation
- Home page navigation
- Global navigation
- Breadcrumbs
Nice to have
• - Sliders
-Drop down navigation

```html
<!DOCTYPE html>
<html lang="en">
<head>
<meta charset="utf-8">
<title>Qorvel Consulting — Data Recovery</title>
<link rel="stylesheet" href="https://fonts.googleapis.com/css2?family=Questrial&family=Oswald:wght@400;500&display=swap">
<style>
:root{
  --red:#ee2d1b;
  --orange:#f07a2a;
  --black:#000;
  --ink:#111;
  --text:#555;
  --muted:#888;
  --panel:#d3d3d3;
  --white:#fff;
  --fb:#3b5998;
  --tw:#2aa3e0;
  --gp:#c9352b;
}
*{margin:0;padding:0;box-sizing:border-box}
html,body{width:1014px;height:1200px;overflow:hidden;background:var(--white)}
body{position:relative;font-family:"Questrial",sans-serif;color:var(--ink)}
.abs{position:absolute}

/* header */
.brand{left:168px;top:44px;font-size:44px;line-height:42px;color:var(--ink);display:flex;align-items:center;gap:8px}
.brand small{display:block;font-size:17px;line-height:20px}
.brand .dot{width:14px;height:14px;background:var(--red);border-radius:50%;flex:none}
.helpline{left:516px;top:42px;display:flex;align-items:center;gap:8px;font-size:13px}
.helpline .need{font-weight:bold;letter-spacing:-.3px}
.helpline .call{color:var(--muted);font-size:11.5px}
.helpline .phone{color:var(--red);font-family:"Oswald",sans-serif;font-size:21px}
.main-nav{left:370px;top:90px;display:flex;align-items:center;height:28px;font-size:14px}
.main-nav a{color:var(--red);text-decoration:none;padding:0 13px;border-left:1px dotted #bbb;line-height:16px}
.main-nav a.current{background:var(--black);color:var(--white);padding:6px 14px;border:0;margin-right:1px}
.main-nav a.current+a{border-left:0}
.main-nav a:last-child{padding-right:0}
.rule{left:168px;top:150px;width:675px;border-top:1px dotted #999}

/* hero */
.hero{left:0;top:152px;width:1014px;height:258px;background:linear-gradient(#fff 10%,#e3e3e3 100%)}
.hero-title{left:192px;top:200px;font-size:24px;line-height:28px;color:var(--red);width:440px;font-weight:normal}
.hero-title b{font-weight:normal;color:var(--ink);font-size:33px}
.hero-title em{font-style:normal;color:var(--ink);font-size:19px}
.hero-note{left:192px;top:273px;font-size:10.5px}
.btn-more{left:192px;top:301px;width:182px;height:43px;background:#2b2b2b;border:1px solid #555;color:var(--white);font-family:"Oswald",sans-serif;font-size:25px;line-height:41px;text-align:center;letter-spacing:.2px}
.hero-art{left:620px;top:164px;width:200px;height:200px;border-radius:6px;background:radial-gradient(circle at 50% 45%,#cfcac3 0,#8a8a8a 55%,#e6e6e6 100%)}
.hero-shadow{left:650px;top:364px;width:170px;height:18px;border-radius:50%;background:radial-gradient(#ccc,transparent 70%)}
.slide-arrow{top:230px}

/* social */
.stay{left:904px;top:164px;width:48px;height:26px;background:#333;color:#fff;font-size:9px;line-height:10px;text-align:center;padding-top:3px;border-radius:2px}
.stay:after{content:"";position:absolute;left:20px;bottom:-5px;border:4px solid transparent;border-top-color:#333;border-bottom:0}
.social{left:908px;width:42px;height:42px;border-radius:50%;border:3px solid #ddd;box-shadow:0 1px 3px rgba(0,0,0,.4)}

/* services */
.band-black{left:0;top:409px;width:1014px;height:93px;background:var(--black)}
.band-gray{left:0;top:502px;width:1014px;height:262px;background:var(--panel)}
.tile{top:400px;width:163px;height:114px;background:#161616;text-align:center;color:var(--white);font-size:14px;line-height:15px;padding-top:70px;box-shadow:0 10px 8px -6px rgba(0,0,0,.35)}
.tile span{color:var(--red)}
.tile.active{background:var(--red)}
.tile.active span{color:var(--white)}
.tile .icon{position:absolute;left:50%;top:10px;width:54px;height:50px;margin-left:-27px;border-radius:6px;background:linear-gradient(#666,#1a1a1a)}
.tile.active .icon{background:linear-gradient(#bbb,#333)}

/* tabs */
.tab{top:560px;height:27px;font-size:12px;line-height:27px;text-align:center;letter-spacing:-.4px;z-index:1}
.tab:before{content:"";position:absolute;inset:0;transform:skewX(-8deg);z-index:-1}
.tab.on{color:#2a2140;font-weight:bold}
.tab.on:before{background:#fff}
.tab.off{color:#fff}
.tab.off:before{background:var(--red)}
.panel{left:192px;top:587px;width:630px;height:144px;background:#fff;box-shadow:0 2px 3px rgba(0,0,0,.15)}
.feature-list{list-style:none;font-size:9.6px;color:var(--text);line-height:15.4px}
.feature-list li{position:relative;padding-left:20px}
.feature-list li:before{content:"";position:absolute;left:1px;top:3px;width:9px;height:9px;border-radius:50%;border:2.5px solid var(--orange);background:#ffd9bd}

/* intro */
.intro-title{left:192px;top:780px;font-family:"Oswald",sans-serif;font-weight:500;font-size:29px;color:var(--red);letter-spacing:-.5px;transform:scaleX(.9);transform-origin:left}
.intro-sub{left:192px;top:818px;font-family:"Oswald",sans-serif;font-size:14.5px;color:#222;transform:scaleX(.9);transform-origin:left}
.intro-text{left:192px;top:845px;width:628px;font-size:9.5px;line-height:15px;color:var(--text)}

/* media */
.band-dark{left:0;top:908px;width:1014px;height:196px;background:var(--black)}
.label-video{left:194px;top:922px;color:#fff;font-family:"Oswald",sans-serif;font-size:14px;line-height:18px;transform:scaleX(.85);transform-origin:left}
.label-testi{left:418px;top:918px;color:#fff;font-family:"Oswald",sans-serif;font-size:25px;transform:scaleX(.85);transform-origin:left}
.video-box{left:193px;top:966px;width:216px;height:151px;background:#fff;border:4px solid #ddd}
.testi-box{left:416px;top:966px;width:407px;height:151px;background:#fff;border:4px solid #ddd}
.portrait{left:430px;top:983px;width:75px;height:80px;background:linear-gradient(#8aa3bb,#3d4f63)}
.quote{left:524px;top:1002px;width:276px;font-size:9px;line-height:12px;color:var(--muted)}
.qmark{font-family:Georgia,serif;font-size:24px;color:#ccc;position:absolute}
.person{left:428px;top:1070px;font-size:11px;color:#222}
.person b{font-family:"Oswald",sans-serif;font-weight:400;font-size:17px;color:var(--red);margin-right:4px}

/* footer */
.foot-links{left:194px;top:1146px;font-size:10px;color:var(--muted)}
.copyright{left:193px;top:1166px;font-size:7.5px;color:#aaa}
.foot-sep{top:1138px;height:42px;border-left:1px solid #ddd}
.foot-contact{left:534px;top:1144px;font-size:10px;color:#555;line-height:18px}
.foot-contact .phone{color:var(--red);font-family:"Oswald",sans-serif;font-size:15px}
.foot-brand{left:736px;top:1138px;font-size:24px;line-height:24px;color:var(--ink);display:flex;align-items:center;gap:5px}
.foot-brand small{display:block;font-size:10px;line-height:11px}
.foot-brand .dot{width:9px;height:9px;background:var(--red);border-radius:50%}
</style>
</head>
<body>

<header>
  <div class="abs brand"><span>qorvel<small>Consulting</small></span><span class="dot"></span></div>
  <div class="abs helpline">
    <span class="need">NEED HELP NOW!</span>
    <svg width="18" height="20" viewBox="0 0 18 20" aria-hidden="true"><path d="M3 2l4 4-2 2c1 3 3 5 6 6l2-2 4 4-3 3C7 18 1 11 1 4z" fill="#222"/></svg>
    <span class="call">Call Us Today:</span>
    <span class="phone">800-555-0142</span>
  </div>
  <nav class="abs main-nav">
    <a class="current" href="#">Home</a>
    <a href="#">Data Recovery</a>
    <a href="#">Penetration Testing</a>
    <a href="#">Company</a>
    <a href="#">Contact</a>
  </nav>
  <div class="abs rule"></div>
</header>

<section>
  <div class="abs hero"></div>
  <h1 class="abs hero-title">Hard Drive <b>Data Recovery</b> is our specialty. <em>Without Compromising On Quality</em></h1>
  <p class="abs hero-note">(we're pretty good at it, too - some BIG organizations rely on us)</p>
  <div class="abs btn-more">MORE DETAILS</div>
  <div class="abs hero-shadow"></div>
  <div class="abs hero-art" role="img" aria-label="Photo of an opened hard drive"></div>
  <svg class="abs slide-arrow" style="left:139px" width="30" height="44" viewBox="0 0 30 44" aria-label="Previous slide"><path d="M26 4L8 22l18 18" stroke="#cfcfcf" stroke-width="8" fill="none"/></svg>
  <svg class="abs slide-arrow" style="left:846px" width="30" height="44" viewBox="0 0 30 44" aria-label="Next slide"><path d="M4 4l18 18L4 40" stroke="#cfcfcf" stroke-width="8" fill="none"/></svg>
</section>

<aside>
  <div class="abs stay">Stay in Touch</div>
  <div class="abs social" style="top:205px;background:var(--fb)" aria-label="Social network"></div>
  <div class="abs social" style="top:255px;background:var(--tw)" aria-label="Social network"></div>
  <div class="abs social" style="top:305px;background:var(--gp)" aria-label="Social network"></div>
</aside>

<section>
  <div class="abs band-black"></div>
  <div class="abs band-gray"></div>
  <div class="abs tile active" style="left:176px"><div class="icon" role="img" aria-label="Hard drive"></div><span>HARD DRIVE</span><br>RECOVERY</div>
  <div class="abs tile" style="left:343px"><div class="icon" role="img" aria-label="USB memory stick"></div><span>MEMORY CARD</span><br>RECOVERY</div>
  <div class="abs tile" style="left:510px"><div class="icon" role="img" aria-label="RAID array unit"></div><span>RAID ARRAY</span><br>RECOVERY</div>
  <div class="abs tile" style="left:678px"><div class="icon" role="img" aria-label="Laptop computer"></div><span>COMPUTER</span><br>FORENSIC</div>

  <div class="abs tab on" style="left:252px;width:124px">WHY US?</div>
  <div class="abs tab off" style="left:384px;width:130px">STEP TO RECOVERY</div>
  <div class="abs tab off" style="left:521px;width:133px">TURN AROUND TIME</div>
  <div class="abs panel"></div>
  <ul class="abs feature-list" style="left:224px;top:617px">
    <li>Free Evaluation</li><li>No Data No Charge</li><li>Class 100 Clean Room Environment</li><li>Forensic Specialists Available</li><li>100% Confidential</li><li>Patent Pending Recovery Technology</li>
  </ul>
  <ul class="abs feature-list" style="left:438px;top:617px">
    <li>High Success Rates</li><li>Free Follow Up Support</li><li>24X7 Lab Operation</li><li>Extensive R&amp;D</li><li>Unparalleled Customer Service</li>
  </ul>
  <ul class="abs feature-list" style="left:608px;top:617px">
    <li>No Hidden Fees</li><li>Fast Turnaround Time</li><li>Free Return Shipment</li><li>Proprietary Hardware and Software</li><li>Recovery From All Types of Media</li>
  </ul>
</section>

<section>
  <h2 class="abs intro-title">Expert Data Recovery Starts Here.</h2>
  <p class="abs intro-sub">Don't worry – you can trust Qorvel Consulting to get you back up and running in no time!</p>
  <p class="abs intro-text">Have you accidentally deleted important files and documents? Dropped or damaged a drive? Is your drive slow to respondor making strange noises? Computer simply won't turn on? Whatever the circumstances of your data loss, our technicians have seen it all, and have the expertise and years of hands-on experience to successfully recover data from any situation, no matter how dire it may seem.</p>
</section>

<section>
  <div class="abs band-dark"></div>
  <div class="abs label-video">LEARN MORE ABOUT<br>OUR DATA RECOVERY PROCESS</div>
  <div class="abs label-testi">OUR CLIENTS TESTIMONIALS</div>
  <div class="abs video-box"></div>
  <svg class="abs" style="left:253px;top:996px" width="88" height="88" viewBox="0 0 88 88" aria-label="Play video">
    <circle cx="44" cy="44" r="40" fill="#fff" stroke="#555" stroke-width="7"/>
    <circle cx="44" cy="44" r="33" fill="#ececec"/>
    <path d="M35 27l26 17-26 17z" fill="#222"/>
  </svg>
  <div class="abs testi-box"></div>
  <div class="abs portrait" role="img" aria-label="Client portrait photo"></div>
  <span class="abs qmark" style="left:522px;top:980px">“</span>
  <p class="abs quote">Lorem ipsum dolor sit amet, consectetuer adipiscing elit, sed diam nonummy nibh euismod tincidunt ut laoreet dolore magna aliquam erat volutpat. Ut wisi enim ad minim veniam, quis nostrud exerci tation ullamcorper suscipit lobortis nisl ut aliquip ex ea commodo consequat.</p>
  <span class="abs qmark" style="left:630px;top:1050px">”</span>
  <div class="abs person"><b>Daniel Whitcombe</b>Senior Partner, President, CEO</div>
</section>

<footer>
  <div class="abs foot-links">Home - Data Recovery - Renetration Testing - Company - Contact</div>
  <div class="abs copyright">Copyright © 2013 qorvel - All rights reserved</div>
  <div class="abs foot-sep" style="left:516px"></div>
  <div class="abs foot-contact">
    <div><svg width="11" height="12" viewBox="0 0 18 20" aria-hidden="true"><path d="M3 2l4 4-2 2c1 3 3 5 6 6l2-2 4 4-3 3C7 18 1 11 1 4z" fill="#777"/></svg> Call Us Today: <span class="phone">800-555-0142</span></div>
    <div><svg width="11" height="9" viewBox="0 0 11 9" aria-hidden="true"><rect x=".5" y=".5" width="10" height="8" fill="none" stroke="#888"/><path d="M.5 .5l5 4 5-4" fill="none" stroke="#888"/></svg> info@qorvelconsulting.example</div>
  </div>
  <div class="abs foot-sep" style="left:712px"></div>
  <div class="abs foot-brand"><span>qorvel<small>Consulting</small></span><span class="dot"></span></div>
</footer>

</body>
</html>
```